Tormelli Welding and Fabrication LLC service truck wrap design

Need an eye catching design for a 2024 Vask crew cab 3500, cab only for Tormelli Welding and Fabrication LLC, relating to a metal working industry. We offer residential handrail fabrication and installation, commercial structural and repair. Please include the company’s logo (can be altered) that will be visible and comprehensible from 50ft away.
Updates

Designs look the same

Target Market(s)

Residential and commercial customers

Industry/Entity Type

Welding and fabrication

Requirements
Must have
• Logo and phone number
Nice to have
• Images involving metal or welding and fabrication

```html
<!DOCTYPE html>
<html lang="en">
<head>
<meta charset="utf-8">
<title>Tormelli Welding and Fabrication LLC – Cab Wrap</title>
<link rel="stylesheet" href="https://fonts.googleapis.com/css2?family=Montserrat:wght@700&family=Oswald:wght@700&display=swap">
<style>
  :root {
    --page: #f2f2f0;
    --wrap-white: #ffffff;
    --wrap-grey: #d9dadc;
    --glass: #2b2f33;
    --band: #111111;
    --tyre: #1c1c1c;
    --hub: #b9bcbf;
    --ink: #231f20;
    --phone-red: #d7263d;
    --accent-red: #d62828;
    --accent-yellow: #f4c20d;
    --band-text: #ffffff;
  }
  * { box-sizing: border-box; margin: 0; padding: 0; }
  html, body { width: 1028px; height: 1200px; overflow: hidden; background: var(--page); }
  .canvas { position: relative; width: 1028px; height: 1200px; }
  .cab-art { position: absolute; inset: 0; }
  .phone {
    position: absolute; display: flex; align-items: center; gap: 8px;
    font-family: "Oswald", sans-serif; font-weight: 700; font-size: 30px;
    color: var(--phone-red); letter-spacing: 0.5px; line-height: 1; white-space: nowrap;
  }
  .phone svg { width: 26px; height: 26px; }
  .brand {
    position: absolute; font-family: "Oswald", sans-serif; font-weight: 700;
    color: var(--ink); text-transform: uppercase; line-height: 1; text-align: center;
  }
  .brand-name { display: block; font-size: 62px; letter-spacing: 1px; }
  .brand-trade { display: block; font-size: 18.5px; letter-spacing: 1.6px; margin-top: 4px; }
  .welder-art {
    position: absolute; border-radius: 14px;
    background: radial-gradient(circle at 45% 75%, var(--accent-yellow) 0 18%, transparent 40%),
                linear-gradient(135deg, var(--accent-red) 0%, #b51f1f 60%, #8e1a1a 100%);
  }
  .web {
    position: absolute; height: 57px; display: flex; align-items: center; justify-content: center;
    font-family: "Montserrat", sans-serif; font-weight: 700;
    font-size: 18px; letter-spacing: 1.3px; color: var(--band-text); text-transform: uppercase;
    line-height: 1; white-space: nowrap;
  }
</style>
</head>
<body>
<main class="canvas">
  <svg class="cab-art" width="1028" height="1200" viewBox="0 0 1028 1200" aria-hidden="true">
    <defs>
      <linearGradient id="rearSweep" x1="0" x2="1" y1="0" y2="0">
        <stop offset="0" stop-color="#ffffff" stop-opacity="0"/>
        <stop offset="1" stop-color="#d9dadc"/>
      </linearGradient>
      <g id="cab-side">
        <rect class="chassis" x="920" y="345" width="108" height="50" fill="#2a2a2a"/>
        <path class="cab-body" d="M28,262 Q30,216 72,212 L385,203 L462,112 Q478,90 522,88 L885,84 Q918,86 922,122 L928,330 L933,455 L112,455 L92,440 L32,420 Z" fill="var(--wrap-white)"/>
        <path class="rear-sweep" d="M700,130 Q760,110 885,110 L928,330 L933,395 L700,395 Z" fill="url(#rearSweep)"/>
        <path class="front-bumper" d="M28,380 L110,386 L112,470 L70,470 L34,430 Z" fill="var(--band)"/>
        <path class="lower-band" d="M368,395 L933,395 L933,452 L368,452 Z" fill="var(--band)"/>
        <path class="door-glass" d="M435,222 L440,160 Q450,118 500,108 L650,104 L650,222 Z" fill="var(--glass)"/>
        <path class="rear-glass" d="M668,100 L840,98 Q858,100 858,120 L858,216 L668,216 Z" fill="var(--glass)"/>
        <path class="headlamp" d="M32,270 L92,268 L96,310 L34,314 Z" fill="#3b3f44"/>
        <path class="wheel-arch" d="M118,470 A125,125 0 0 1 366,470 Z" fill="var(--band)"/>
        <circle class="tyre" cx="242" cy="476" r="100" fill="var(--tyre)"/>
        <circle class="hub" cx="242" cy="476" r="58" fill="var(--hub)"/>
        <circle class="hub-cap" cx="242" cy="476" r="22" fill="#8d9195"/>
        <rect class="mirror" x="345" y="160" width="46" height="60" rx="8" fill="var(--band)"/>
        <rect class="door-handle" x="508" y="236" width="52" height="12" rx="5" fill="#333"/>
        <rect class="door-handle" x="742" y="228" width="52" height="12" rx="5" fill="#333"/>
        <line class="door-seam" x1="655" y1="100" x2="660" y2="395" stroke="#c9cacc" stroke-width="2"/>
        <line class="door-seam" x1="385" y1="205" x2="372" y2="395" stroke="#c9cacc" stroke-width="2"/>
      </g>
    </defs>
    <use href="#cab-side" class="driver-side"/>
    <use href="#cab-side" class="passenger-side" transform="translate(1028,567) scale(-1,1)"/>
  </svg>

  <!-- Driver side -->
  <div class="phone" style="left:111px; top:276px;">
    <svg viewBox="0 0 24 24"><path fill="#231f20" d="M6.6 10.8a15.1 15.1 0 0 0 6.6 6.6l2.2-2.2a1 1 0 0 1 1-.25 11.4 11.4 0 0 0 3.6.57 1 1 0 0 1 1 1V20a1 1 0 0 1-1 1A17 17 0 0 1 3 4a1 1 0 0 1 1-1h3.5a1 1 0 0 1 1 1c0 1.25.2 2.45.57 3.57a1 1 0 0 1-.25 1z"/></svg>
    555-014-8260
  </div>
  <div class="brand" style="left:386px; top:283px; width:312px;">
    <span class="brand-name">Tormelli</span>
    <span class="brand-trade">Welding and Fabrication LLC</span>
  </div>
  <div class="welder-art" role="img" aria-label="Illustration of a welder in a red jacket and helmet, sparks flying" style="left:742px; top:240px; width:188px; height:152px;"></div>
  <div class="web" style="left:368px; top:395px; width:565px;">tormelliweldingandfabrication.com</div>

  <!-- Passenger side -->
  <div class="phone" style="left:700px; top:843px;">
    <svg viewBox="0 0 24 24"><path fill="#231f20" d="M6.6 10.8a15.1 15.1 0 0 0 6.6 6.6l2.2-2.2a1 1 0 0 1 1-.25 11.4 11.4 0 0 0 3.6.57 1 1 0 0 1 1 1V20a1 1 0 0 1-1 1A17 17 0 0 1 3 4a1 1 0 0 1 1-1h3.5a1 1 0 0 1 1 1c0 1.25.2 2.45.57 3.57a1 1 0 0 1-.25 1z"/></svg>
    555-014-8260
  </div>
  <div class="brand" style="left:328px; top:850px; width:312px;">
    <span class="brand-name">Tormelli</span>
    <span class="brand-trade">Welding and Fabrication LLC</span>
  </div>
  <div class="welder-art" role="img" aria-label="Illustration of a welder in a red jacket and helmet, sparks flying" style="left:98px; top:807px; width:188px; height:152px;"></div>
  <div class="web" style="left:95px; top:962px; width:565px;">tormelliweldingandfabrication.com</div>
</main>
</body>
</html>
```